Can Design for Fun, Growing Health Food Brand

We are launching a brand new product, electrolyte seltzer drinks. We want the design to be clean/simple and slightly modern while staying true to our brand identity. Must say "Mineral Hydration" as the product descriptor, sub headline is "Carbonated electrolyte beverage with sea moss and real fruit juice". First flavors will be Watermelon Mint and Mango.

Target Market(s)

Women ages 30-50 who are interested in health wellness/trends

Industry/Entity Type

Health & Wellness

Font styles to use
Sans Serif

Requirements
Must have
• Tall, skinny can, current Bright Kelp Co Logo, use aluminum on can as element in design.
Nice to have
• Be fun, clean and modern. Would like to see the label less busy than our gels.
Should not have
• Avoid putting flavor on bottom 1/5 of can. No gradient color changes. Do not want really detailed or realistic fruit image, prefer drawings or similar.

```html
<!DOCTYPE html>
<html lang="en">
<head>
<meta charset="utf-8">
<title>Bright Kelp Co – Mineral Hydration Cans</title>
<link href="https://fonts.googleapis.com/css2?family=Roboto+Condensed:wght@300;400;700&display=swap" rel="stylesheet">
<style>
  :root{
    --paper:#ffffff;
    --ink:#0d0d0d;
    --label:#ffffff;
    --lid:#9ea3a6;
    --melon-can:#72f27e;
    --melon-band:#3e9a70;
    --melon-art:#d9f5de;
    --mango-can:#f26b43;
    --mango-band:#f86a45;
    --mango-art:#fbd2c2;
  }
  *{margin:0;padding:0;box-sizing:border-box}
  html,body{width:846px;height:1200px;overflow:hidden;background:var(--paper)}
  .canvas{position:relative;width:846px;height:1200px;background:var(--paper);font-family:"Roboto Condensed",sans-serif}
  .can{position:absolute;top:236px;width:262px;height:660px}
  .can--melon{left:107px;--body:var(--melon-can);--band:var(--melon-band);--art:var(--melon-art)}
  .can--mango{left:470px;--body:var(--mango-can);--band:var(--mango-band);--art:var(--mango-art)}
  .can__shape{position:absolute;inset:0}
  .can__body{fill:var(--body)}
  .can__lid{fill:var(--lid)}
  .can__label{fill:var(--label)}
  .can__band{fill:var(--band)}
  .can__text{position:absolute;left:0;width:262px;text-align:center;line-height:1}
  .brand{top:130px;display:flex;justify-content:center;align-items:center;gap:7px;font-size:26px;font-weight:400;color:var(--ink);letter-spacing:-0.8px}
  .brand__dot{width:13px;height:13px;border-radius:50%;background:var(--ink)}
  .descriptor{top:172px;font-size:40px;font-weight:700;color:var(--ink);line-height:35px;letter-spacing:-0.8px}
  .flavor{top:255px;font-size:21px;font-weight:700;color:var(--ink);letter-spacing:-0.2px}
  .subline{top:325px;font-size:21px;font-weight:400;color:var(--label);line-height:23.5px;letter-spacing:0.2px}
  .fruit-art{position:absolute;left:64px;top:458px;width:134px;height:104px;border-radius:50%;background:var(--art)}
  .volume{top:578px;font-size:22px;font-weight:300;color:var(--label);word-spacing:8px}
</style>
</head>
<body>
<main class="canvas">

  <section class="can can--melon">
    <svg class="can__shape" viewBox="0 0 262 660" aria-hidden="true">
      <path class="can__body" d="M31 14 H231 Q236 30 248 44 Q262 60 262 86 V628 Q262 652 231 656 H31 Q0 652 0 628 V86 Q0 60 14 44 Q26 30 31 14 Z"/>
      <rect class="can__lid" x="31" y="2" width="200" height="12" rx="3"/>
      <path class="can__label" d="M18 86 Q50 86 74 80 Q131 60 188 80 Q212 86 244 86 V304 Q212 304 188 298 Q131 278 74 298 Q50 304 18 304 Z"/>
      <path class="can__band" d="M18 304 Q50 304 74 298 Q131 278 188 298 Q212 304 244 304 V524 Q225 528 210 524 H52 Q37 528 18 524 Z"/>
    </svg>
    <div class="can__text brand"><span class="brand__dot"></span>BRIGHT KELP CO</div>
    <h2 class="can__text descriptor">MINERAL<br>HYDRATION</h2>
    <p class="can__text flavor">WATERMELON MINT</p>
    <p class="can__text subline">CARBONATED<br>ELECTROLYTE<br>BEVERAGE WITH<br>SEA MOSS AND<br>REAL FRUIT JUICE</p>
    <div class="fruit-art" role="img" aria-label="Line drawing of a watermelon slice with mint leaves"></div>
    <p class="can__text volume">12oz | 355ml</p>
  </section>

  <section class="can can--mango">
    <svg class="can__shape" viewBox="0 0 262 660" aria-hidden="true">
      <path class="can__body" d="M31 14 H231 Q236 30 248 44 Q262 60 262 86 V628 Q262 652 231 656 H31 Q0 652 0 628 V86 Q0 60 14 44 Q26 30 31 14 Z"/>
      <rect class="can__lid" x="31" y="2" width="200" height="12" rx="3"/>
      <path class="can__label" d="M18 86 Q50 86 74 80 Q131 60 188 80 Q212 86 244 86 V304 Q212 304 188 298 Q131 278 74 298 Q50 304 18 304 Z"/>
      <path class="can__band" d="M18 304 Q50 304 74 298 Q131 278 188 298 Q212 304 244 304 V524 Q225 528 210 524 H52 Q37 528 18 524 Z"/>
    </svg>
    <div class="can__text brand"><span class="brand__dot"></span>BRIGHT KELP CO</div>
    <h2 class="can__text descriptor">MINERAL<br>HYDRATION</h2>
    <p class="can__text flavor">MANGO</p>
    <p class="can__text subline">CARBONATED<br>ELECTROLYTE<br>BEVERAGE WITH<br>SEA MOSS AND<br>REAL FRUIT JUICE</p>
    <div class="fruit-art" role="img" aria-label="Line drawing of a whole mango and a halved mango with leaves"></div>
    <p class="can__text volume">12oz | 355ml</p>
  </section>

</main>
</body>
</html>
```